Food company business card needs a freshen up

A little bit about our business. Wholesale Food Company (Velo Supply PNG Ltd) with a number of retail businesses including a Deli Butchery/Bakery (named The Brava Grill Shed) and Fast-Food Restaurants (Tornado Wrap, Yam Tart Bun, Reefies) and a catering company called Brava Lulu Catering. At our head office (Velo Supply) we also have 2 manufacturing factories - Bakery (Brava Oven Shed products) and Butchery (Brava Fine products). We are proudly 100% PNG owned - this could be good to include somewhere on the business card.
Our current website is:
www.vsx-trade.com.pg
Please visit our website for further design aesthetics that we would like to tie into our business cards and information can be found on our website. Colour schemes are red, black and white.
We have a previous draft business card (attached) that we want to be improved to match our new website aesthetics.
We would like to make the business cards portrait and individualised for each of our staff members that require them and would like these to be editable to change the details when needed. We want these to be modern, professional and visually engaging with the use of photos (stock images used in our draft). If we can get photos of meat/sausages, fresh uncooked chicken, fresh fish, potato fries, cheese burger, bread roll/pies, and vegetables (make it look green and fresh) – these should be generic photos and product focused.
Constant information we want to see on the business cards.
1. Velo Supply PNG LTD
- Wholesale Food Sales & Delivery
- Butchery Manufacturing
- Bakery Manufacturing
- Quality Assurance
- Customs & Freight
- Retail
- Catering & Equipment Hire
2. Website – www.vsx-trade.com.pg
3. Phone – 487 2615 / 487 2648
4. Address – Sec 212, Lot 58. Wenrick Rd, Torumai
5. And logos of all our retail brands.
I have attached each of our logos. I have also attached a tribal fish design which we use on all business cards, email signatures and uniforms across all sites.
- Velo Supply Logo
- Grill Shed Logo
- Tornado Wrap Logo
- Reefies Logo
- Yam Tart Bun Logo
- Brava Lulu Catering Logo
- Oven Shed Logo (for Velo Supply - Bakery Factory Products)
- Brava Fine logo (for Velo Supply - Butchery Factory Products)
- HACCAP logo (Quality Assurance cert of our Butchery Factory)
Information that will change:
Name – e.g. Liam Corder
Title – Marketing & Promotions
Email –liamcorder@velosupplypng-demo.com.pg
Mobile – (+675 7222 2222)
Please use Liam Corder as an example in your designs.
Thank you and looking forward to your designs :)
Miriam
Local and International Clients
Food Industry
See detailed brief

```html
<!DOCTYPE html>
<html lang="en">
<head>
<meta charset="utf-8">
<title>Velo Supply PNG LTD – Business Card</title>
<link rel="stylesheet" href="https://fonts.googleapis.com/css2?family=Oswald:wght@500;600&family=Poppins:wght@400;500;600&display=swap">
<style>
  :root {
    --backdrop: #c9c9c9;
    --brand-red: #ad1d25;
    --blush: #f8cbd3;
    --ink: #1c1c1c;
    --white: #ffffff;
  }
  * { box-sizing: border-box; margin: 0; padding: 0; }
  html, body { width: 1200px; height: 1101px; overflow: hidden; }
  body {
    background: var(--backdrop);
    position: relative;
    font-family: "Poppins", sans-serif;
    color: var(--ink);
  }
  .card {
    position: absolute;
    top: 264px;
    width: 308px;
    height: 540px;
    overflow: hidden;
  }
  .card--front { left: 243px; }
  .card--back { left: 640px; background: var(--white); }

  /* Front */
  .front-photo {
    position: absolute; inset: 0 0 auto 0; height: 319px;
    background:
      radial-gradient(circle at 20% 20%, #4f8f3a 0, transparent 45%),
      radial-gradient(circle at 80% 25%, #6fa84a 0, transparent 40%),
      radial-gradient(circle at 15% 80%, #a0242c 0, transparent 35%),
      radial-gradient(circle at 85% 80%, #d9b34a 0, transparent 35%),
      linear-gradient(160deg, #3f7a33, #7c9a4c 50%, #8a4a34);
  }
  .price-tag {
    position: absolute; left: 91px; top: 52px; width: 128px; height: 223px;
  }
  .tag-wordmark {
    position: absolute; left: 91px; top: 110px; width: 128px;
    text-align: center; font-family: "Oswald", sans-serif; color: #111;
  }
  .tag-wordmark .line-big { display: block; font-weight: 600; font-size: 38px; line-height: 1.05; }
  .tag-wordmark .line-rule { display: block; margin: 6px 12px 4px; border-top: 1.5px dotted #333; }
  .tag-wordmark .line-small { display: block; font-weight: 500; font-size: 27px; line-height: 1.15; }
  .services {
    position: absolute; left: 0; right: 0; top: 319px; bottom: 0;
    background: var(--brand-red); color: var(--white);
    list-style: none; padding: 29px 0 0 26px;
    font-size: 15.5px; line-height: 23.6px;
  }
  .services li::before { content: "•"; margin-right: 5px; }

  /* Back */
  .back-info {
    position: absolute; inset: 0 0 auto 0; height: 404px;
    background: var(--blush);
  }
  .company-mark {
    position: absolute; right: 28px; top: 52px;
    display: flex; align-items: center; gap: 7px;
    font-family: "Oswald", sans-serif; font-weight: 600; font-size: 24px; color: var(--brand-red);
  }
  .company-mark .dot { width: 14px; height: 14px; border-radius: 50%; background: var(--brand-red); }
  .person-name {
    position: absolute; left: 30px; top: 113px;
    font-family: "Oswald", sans-serif; font-weight: 600; font-size: 30px; line-height: 1; color: var(--brand-red);
  }
  .person-title { position: absolute; left: 30px; top: 149px; font-size: 16px; line-height: 1.1; }
  .rule { position: absolute; left: 24px; right: 29px; border-top: 1.5px dotted #444; }
  .rule--top { top: 182px; }
  .rule--bottom { top: 337px; }
  .contact { position: absolute; left: 27px; right: 24px; top: 200px; font-size: 14.5px; line-height: 21.5px; white-space: nowrap; }
  .contact b { font-weight: 600; }
  .contact .email { font-size: 11.2px; }
  .address { position: absolute; left: 27px; top: 272px; font-size: 14.5px; line-height: 19.5px; }
  .web-row {
    position: absolute; left: 25px; right: 29px; top: 360px;
    display: flex; justify-content: space-between; align-items: center;
  }
  .website { font-family: "Oswald", sans-serif; font-weight: 500; font-size: 17px; line-height: 1; color: #111; white-space: nowrap; }
  .cert-badge { flex: none; width: 56px; height: 26px; border-radius: 4px; background: var(--brand-red); }
  .brand-strip {
    position: absolute; left: 0; right: 0; top: 404px; bottom: 0;
    display: flex; flex-direction: column; justify-content: center; gap: 24px;
    padding: 0 14px;
  }
  .brand-row { display: flex; justify-content: space-around; align-items: center; }
  .brand {
    display: flex; align-items: center; gap: 4px; white-space: nowrap;
    font-size: 10px; font-weight: 600; color: var(--ink); line-height: 1;
  }
  .brand::before {
    content: ""; flex: none; width: 7px; height: 7px; border-radius: 50%; background: var(--brand-red);
  }
</style>
</head>
<body>

<section class="card card--front">
  <div class="front-photo" role="img" aria-label="Top-down photo of fresh vegetables and salad ingredients in bowls"></div>
  <svg class="price-tag" viewBox="0 0 128 223" aria-hidden="true">
    <path d="M0 36 L40 0 L88 0 L128 36 L128 223 L0 223 Z" fill="rgba(255,255,255,0.72)"/>
    <circle cx="64" cy="30" r="9" fill="#7c9a4c"/>
  </svg>
  <h1 class="tag-wordmark">
    <span class="line-big">VELO</span>
    <span class="line-big">SUPPLY</span>
    <span class="line-rule"></span>
    <span class="line-small">PNG LTD</span>
  </h1>
  <ul class="services">
    <li>Wholesale Food Sales &amp; Delivery</li>
    <li>Butchery Manufacturing</li>
    <li>Bakery Manufacturing</li>
    <li>Quality Assurance</li>
    <li>Customs &amp; Freight</li>
    <li>Retail</li>
    <li>Catering &amp; Equipment Hire</li>
  </ul>
</section>

<section class="card card--back">
  <div class="back-info">
    <div class="company-mark"><span class="dot"></span>Velo Supply</div>
    <h2 class="person-name">Liam Corder</h2>
    <p class="person-title">Marketing &amp; Promotions</p>
    <div class="rule rule--top"></div>
    <p class="contact">
      <b>Phone:</b> 487 2615/487 2648<br>
      <b>Mobile:</b> +675 7222 2222<br>
      <span class="email">liamcorder@velosupplypng-demo.com.pg</span>
    </p>
    <p class="address">Sec 212, Lot 58.<br>Wenrick Rd, Torumai</p>
    <div class="rule rule--bottom"></div>
    <div class="web-row">
      <span class="website">WWW.VSX-TRADE.COM.PG</span>
      <span class="cert-badge" aria-label="Quality certification badge"></span>
    </div>
  </div>
  <div class="brand-strip">
    <div class="brand-row">
      <span class="brand">Tornado Wrap</span>
      <span class="brand">Brava Lulu</span>
      <span class="brand">Reefies</span>
      <span class="brand">Grill Shed</span>
    </div>
    <div class="brand-row">
      <span class="brand">Yam Tart Bun</span>
      <span class="brand">Brava Oven Shed</span>
      <span class="brand">Brava Fine</span>
    </div>
  </div>
</section>

</body>
</html>
```